Professional law firm looking for new professional and eye-catching business card design

Law firm in need of new business card design using existing firm logo and firm colors on thick card stock. Firm colors are navy blue, cyan blue, and gray. Please use firm's logo either on the back of the card or on the front and back. I am looking for something eye-catching and resonating but also professional.

Target Market(s)

Law firm growth by attracting clients with professional, creative, and attractive business cards.

Industry/Entity Type

Legal/Law Firm

Contact Information for Business Card

Name: Derek T. Halloway, Esq., Address: 517 E. Quintley Blvd., P.O. Box 641, Tavares, FL 32790, Phone numbers: (352) 555-0187 Office, (352) 555-0142 Fax, email address: DerekH@hqlegalfx.com, website: www.HQLegalFX.com

Font styles to use
Other font styles liked:
• Font as close as possible to matching law firm logo.

Requirements
Must have
• Must have business card details and law firm logo with law firm colors.

```html
<!DOCTYPE html>
<html lang="en">
<head>
<meta charset="utf-8">
<title>HQ Legal – Business Card</title>
<link href="https://fonts.googleapis.com/css2?family=Crimson+Text:wght@400;600&family=Source+Sans+3:wght@500;600&display=swap" rel="stylesheet">
<style>
  :root {
    --backdrop: #4b4b4b;
    --navy: #18202c;
    --cyan: #1aa3df;
    --cyan-text: #1b8fc9;
    --gray: #a9a9ad;
    --serif: "Crimson Text", Georgia, serif;
    --sans: "Source Sans 3", Arial, sans-serif;
  }
  * { box-sizing: border-box; margin: 0; padding: 0; }
  html, body { width: 1200px; height: 900px; overflow: hidden; }
  body { background: var(--backdrop); position: relative; }

  .card {
    position: absolute;
    left: 250px;
    width: 700px;
    height: 388px;
    background: var(--navy);
    overflow: hidden;
  }
  .card--front { top: 46px; }
  .card--back { top: 466px; }

  .rule { position: absolute; height: 2px; background: var(--gray); }
  .card--front .rule--left { left: 0; top: 193px; width: 212px; }
  .card--front .rule--right { right: 0; top: 193px; width: 212px; }

  .firm-mark {
    position: absolute;
    display: flex;
    flex-direction: column;
    align-items: flex-start;
    color: var(--cyan);
    font-family: var(--serif);
    font-weight: 600;
  }
  .firm-mark__name { font-size: 48px; line-height: 1; letter-spacing: 3px; }
  .firm-mark__line { width: 100%; height: 2px; background: var(--gray); margin: 6px 0 5px; }
  .firm-mark__sub { font-size: 14px; font-variant: small-caps; letter-spacing: 0.5px; line-height: 1; }

  .card--front .firm-mark { left: 232px; top: 158px; width: 236px; }
  .card--back .firm-mark { left: 90px; top: 168px; width: 236px; }

  .contact {
    position: absolute;
    left: 364px;
    top: 76px;
    right: 0;
  }
  .contact__name {
    font-family: var(--serif);
    font-variant: small-caps;
    font-size: 25px;
    color: var(--cyan);
    letter-spacing: 0.3px;
    line-height: 1;
  }
  .contact__rule { height: 2px; background: var(--gray); margin: 8px 0 14px; }
  .contact__group { margin-bottom: 14px; }
  .contact__item {
    display: flex;
    align-items: flex-start;
    gap: 3px;
    font-family: var(--sans);
    font-weight: 500;
    font-size: 19px;
    line-height: 25px;
    color: var(--cyan-text);
  }
  .contact__item svg { width: 22px; height: 20px; flex: none; margin-top: 3px; fill: var(--cyan-text); }
</style>
</head>
<body>

  <section class="card card--front" aria-label="Card front">
    <div class="rule rule--left"></div>
    <div class="firm-mark">
      <span class="firm-mark__name">HQ LEGAL</span>
      <span class="firm-mark__line"></span>
      <span class="firm-mark__sub">Halloway &amp; Quinn, P.A.</span>
    </div>
    <div class="rule rule--right"></div>
  </section>

  <section class="card card--back" aria-label="Card back">
    <div class="firm-mark">
      <span class="firm-mark__name">HQ LEGAL</span>
      <span class="firm-mark__line"></span>
      <span class="firm-mark__sub">Halloway &amp; Quinn, P.A.</span>
    </div>

    <div class="contact">
      <h1 class="contact__name">Derek T. Halloway, Esq.</h1>
      <div class="contact__rule"></div>

      <div class="contact__group">
        <p class="contact__item">
          <svg viewBox="0 0 22 20" aria-hidden="true"><path d="M2 6c0-3 4-4 9-4s9 1 9 4v2h-5V6H7v2H2z"/><path d="M5 9h12l3 9H2z"/></svg>
          (352) 555-0187
        </p>
        <p class="contact__item">
          <svg viewBox="0 0 22 20" aria-hidden="true"><rect x="6" y="1" width="10" height="6"/><rect x="2" y="8" width="18" height="7" rx="1"/><rect x="6" y="13" width="10" height="6"/></svg>
          (352) 555-0142
        </p>
      </div>

      <div class="contact__group">
        <p class="contact__item">
          <svg viewBox="0 0 22 20" aria-hidden="true"><path d="M1 4h20v12H1z"/><path d="M1 4l10 7 10-7" fill="none" stroke="#18202c" stroke-width="1.6"/></svg>
          DerekH@hqlegalfx.com
        </p>
        <p class="contact__item">
          <svg viewBox="0 0 22 20" aria-hidden="true"><circle cx="11" cy="10" r="8.5" fill="none" stroke="#1b8fc9" stroke-width="1.6"/><ellipse cx="11" cy="10" rx="3.5" ry="8.5" fill="none" stroke="#1b8fc9" stroke-width="1.4"/><path d="M2.5 10h17M4 5.5h14M4 14.5h14" stroke="#1b8fc9" stroke-width="1.4"/></svg>
          www.HQLegalFX.com
        </p>
      </div>

      <div class="contact__group">
        <p class="contact__item">
          <svg viewBox="0 0 22 20" aria-hidden="true"><path d="M11 0a7 7 0 0 1 7 7c0 5-7 13-7 13S4 12 4 7a7 7 0 0 1 7-7z"/><circle cx="11" cy="7" r="2.6" fill="#18202c"/></svg>
          <span>517 E. Quintley Blvd.,<br>P.O. Box 641, Tavares, FL 32790</span>
        </p>
      </div>
    </div>
  </section>

</body>
</html>
```